Fernwick

We require a professional design for a Cosmetic Surgery college. We have just submitted the request for our new logo which will be used on this card. We are the leaders in our field of education in Australia and this should be reflected in the quality of the card. People want to come and study with us because we are so outstanding in the field. Studying with us provides credibility, quality and courage.
Updates

Project Deadline Extended
Reason: Require updated logo to be used in design

Target Market(s)

25 - 40 year old professional women primarily from a medical background wanting to continue study in the cosmetic medical field, western speaking countries. The course average cost is 17k AU for 16 weeks.

Industry/Entity Type

Education

Requirements
Must have
• Must us the logo that is currently under design by this company.
Nice to have
• A medical twist very subtle would be nice possilbly rod of Asclepius.
Should not have
• Should not look old, we are dealing with modern medical concepts.
The logo that is being redesigned 3d silver, the attached logo is the old one.

```html
<!DOCTYPE html>
<html lang="en">
<head>
<meta charset="utf-8">
<title>Fernwick – Business Card</title>
<link rel="stylesheet" href="https://fonts.googleapis.com/css2?family=Open+Sans:wght@400;600;700&display=swap">
<style>
  :root {
    --backdrop: #e6e6e6;
    --paper: #ffffff;
    --ink: #1e1e1e;
    --ink-soft: #3a3a3a;
    --teal: #0f7f94;
    --teal-deep: #0b5c7a;
    --teal-bright: #0799aa;
    --white: #ffffff;
  }
  * { box-sizing: border-box; margin: 0; padding: 0; }
  html, body {
    width: 1200px; height: 720px; overflow: hidden;
    background: var(--backdrop);
    font-family: "Open Sans", Arial, sans-serif;
  }
  .canvas { position: relative; width: 1200px; height: 720px; }

  .card {
    position: absolute; top: 240px;
    width: 420px; height: 240px;
    overflow: hidden;
  }
  .card--front { left: 147px; background: var(--paper); }
  .card--back {
    left: 633px;
    background: linear-gradient(160deg, var(--teal-bright) 0%, var(--teal) 45%, var(--teal-deep) 100%);
  }

  /* brand lockup */
  .brand { position: absolute; display: flex; align-items: center; gap: 12px; }
  .brand__dot { border-radius: 50%; flex: none; }
  .brand__name { font-weight: 600; letter-spacing: 0.02em; line-height: 1; }

  .card--front .brand { left: 21px; top: 40px; }
  .card--front .brand__dot { width: 56px; height: 56px; background: var(--teal); }
  .card--front .brand__name { font-size: 34px; color: var(--teal); }

  .card--back .brand { left: 51px; top: 92px; gap: 14px; }
  .card--back .brand__dot { width: 64px; height: 64px; background: var(--white); }
  .card--back .brand__name { font-size: 38px; color: var(--white); }

  /* person */
  .person { position: absolute; left: 28px; top: 126px; }
  .person__name { font-size: 13px; color: var(--ink); line-height: 1.2; }
  .person__name strong { font-weight: 700; }
  .person__title {
    font-size: 10px; color: var(--teal); letter-spacing: 0.18em;
    font-weight: 600; margin-top: 2px;
  }

  /* contact */
  .contact { position: absolute; left: 28px; top: 165px; list-style: none; }
  .contact__item {
    display: flex; align-items: center; gap: 7px;
    font-size: 10px; color: var(--ink-soft); height: 16px;
  }
  .contact__icon { width: 9px; height: 9px; flex: none; }
  .contact__item--web { font-weight: 700; color: var(--teal-deep); }

  .address {
    position: absolute; right: 29px; top: 165px;
    text-align: right; font-style: normal;
    font-size: 10px; color: var(--ink-soft); line-height: 16px;
  }
  .address__label { font-weight: 700; color: var(--ink); letter-spacing: 0.02em; }

  .card__band {
    position: absolute; left: 0; bottom: 0; width: 100%; height: 10px;
    background: linear-gradient(90deg, var(--teal-deep), var(--teal-bright));
  }
</style>
</head>
<body>
<main class="canvas">

  <section class="card card--front" aria-label="Business card front">
    <div class="brand">
      <span class="brand__dot"></span>
      <span class="brand__name">FERNWICK</span>
    </div>

    <div class="person">
      <p class="person__name">NAME <strong>SURENAME</strong></p>
      <p class="person__title">YOUR TITLE</p>
    </div>

    <ul class="contact">
      <li class="contact__item">
        <svg class="contact__icon" viewBox="0 0 10 10" aria-hidden="true">
          <path d="M2 0.5 L3.6 0.5 L4.2 2.8 L3.1 3.6 Q4 5.8 6.3 6.9 L7.2 5.8 L9.5 6.4 L9.5 8 Q9.5 9.5 8 9.5 Q1 8.8 0.5 2 Q0.5 0.5 2 0.5 Z" fill="var(--teal)"/>
        </svg>
        + 33 140 512 686
      </li>
      <li class="contact__item">
        <svg class="contact__icon" viewBox="0 0 10 10" aria-hidden="true">
          <rect x="0.6" y="2" width="8.8" height="6" fill="none" stroke="var(--teal)" stroke-width="1"/>
          <path d="M0.6 2 L5 5.4 L9.4 2" fill="none" stroke="var(--teal)" stroke-width="1"/>
        </svg>
        contact@fernwickmail.com
      </li>
      <li class="contact__item contact__item--web">www.fernwickmedicalae.com</li>
    </ul>

    <address class="address">
      <span class="address__label">YOUR COMPANY ADDRESS</span><br>
      48 rue des Lilas Verts<br>
      75011 Paris
    </address>

    <div class="card__band"></div>
  </section>

  <section class="card card--back" aria-label="Business card back">
    <div class="brand">
      <span class="brand__dot"></span>
      <span class="brand__name">FERNWICK</span>
    </div>
  </section>

</main>
</body>
</html>
```